Vostran, Pemmel & Co.
Project: Brochure
Brochure
Individuals, Corporations, Non - Profit organizations & small business and Ledgerfox users.
New Logo Attached Word File I would like either a tri fold brochure but leaning twards a brochure that is 11 inch height by 5 inch wide which would have 4 pages - Cover, 2 inside pages & back cover. Probably a better fit since I do not have a lot of content. Maybe a picture that would be appropriate also.

```html
<!DOCTYPE html>
<html lang="en">
<head>
<meta charset="utf-8">
<title>Vostran, Pemmel &amp; Co. — Brochure</title>
<link rel="stylesheet" href="https://fonts.googleapis.com/css2?family=Cinzel:wght@600&family=Open+Sans:wght@400;600;700&family=Raleway:wght@300;400&display=swap">
<style>
  :root{
    --ground:#e6e0d8;
    --brown-deep:#2f1d13;
    --brown:#4a2e1d;
    --brown-mid:#6e4529;
    --copper:#c8792c;
    --cream:#f4eee6;
    --paper:#ffffff;
    --text-light:#e9ddcf;
    --text-muted:#bda68f;
    --ink:#3a2619;
  }
  *{box-sizing:border-box;margin:0;padding:0}
  html,body{width:1200px;height:792px;overflow:hidden;background:var(--ground)}
  body{font-family:"Open Sans",Arial,sans-serif;position:relative}

  .trifold{position:absolute;left:40px;top:72px;width:840px;height:648px;display:flex;box-shadow:0 4px 18px rgba(0,0,0,.18)}
  .panel{width:280px;height:100%;position:relative;overflow:hidden}
  .rack-card{position:absolute;left:920px;top:132px;width:240px;height:528px;box-shadow:0 4px 18px rgba(0,0,0,.18);overflow:hidden}

  .photo{position:absolute;left:0;width:100%}
  .photo--dominoes{top:0;height:150px;background:linear-gradient(135deg,#f5f1ea 0%,#d9cfc2 55%,#b99c7c 100%)}
  .photo--meeting{bottom:0;height:120px;background:linear-gradient(120deg,#dfe4ea 0%,#c6ccd3 50%,#8a8f96 100%)}
  .photo--analyst{top:0;height:200px;background:linear-gradient(135deg,#eef0f2 0%,#b9b3ad 55%,#3e3630 100%)}
  .photo--team{background:linear-gradient(150deg,#f1efec 0%,#cfc6bc 45%,#5b4a3d 100%);border:3px solid var(--copper)}

  /* panel one */
  .panel--services{background:var(--brown)}
  .services{position:absolute;top:150px;left:0;right:0;bottom:120px;padding:24px 26px 0;background:linear-gradient(180deg,var(--brown-mid),var(--brown))}
  .section-title{font-family:"Open Sans",Arial,sans-serif;font-weight:700;font-size:14px;letter-spacing:.6px;color:var(--copper);text-transform:uppercase;line-height:1.25;margin-bottom:14px}
  .services p{font-size:9.5px;line-height:1.6;color:var(--text-light);margin-bottom:10px}

  /* panel two */
  .panel--clients{background:var(--paper)}
  .clients{position:absolute;top:200px;left:0;right:0;height:250px;background:linear-gradient(180deg,var(--brown-mid),var(--brown));padding:26px 26px 0}
  .client-list{list-style:none;display:grid;grid-template-columns:1fr 1fr;gap:7px 14px}
  .client-list li{font-size:10.5px;color:var(--text-light);display:flex;align-items:center;gap:7px}
  .client-list li::before{content:"";width:6px;height:6px;background:var(--copper);flex:none}
  .contact{position:absolute;top:450px;left:0;right:0;bottom:0;padding:30px 26px;background:var(--paper)}
  .brand{display:flex;align-items:center;gap:10px}
  .brand__mark{width:26px;height:26px;background:var(--copper);flex:none}
  .brand__name{font-family:"Cinzel",Georgia,serif;font-weight:600;font-size:15px;color:var(--ink);letter-spacing:.3px}
  .brand__tag{font-size:7.5px;letter-spacing:1.4px;text-transform:uppercase;color:var(--copper);margin:4px 0 0 36px}
  .address{margin:18px 0 0 36px;font-size:9.5px;line-height:1.6;color:var(--ink)}

  /* cover */
  .cover{background:linear-gradient(180deg,var(--brown-deep),var(--brown) 70%,var(--brown-deep))}
  .cover .brand{position:absolute;left:20px;right:16px}
  .cover .brand__name{color:var(--cream)}
  .cover .brand__tag{color:var(--text-muted)}
  .cover__rule{position:absolute;left:0;right:0;height:2px;background:var(--copper)}
  .cover__lines{font-family:"Raleway",Arial,sans-serif;font-weight:300;color:var(--cream);text-transform:uppercase;letter-spacing:1px;position:absolute}
  .cover__lines .since{text-transform:none;color:var(--text-muted)}
  .cover__web{position:absolute;left:0;right:0;text-align:center;color:var(--text-muted);font-size:10px;letter-spacing:.5px}

  .panel.cover .brand{top:26px}
  .panel.cover .brand-tag-wrap{position:absolute;top:54px;left:20px}
  .panel.cover .cover__rule{top:84px}
  .panel.cover .photo--team{top:100px;left:22px;width:236px;height:250px}
  .panel.cover .cover__lines{left:120px;top:410px;font-size:15px;line-height:1.35}
  .panel.cover .cover__web{bottom:24px}

  .rack-card .brand{top:22px}
  .rack-card .brand__name{font-size:13px}
  .rack-card .brand-tag-wrap{position:absolute;top:46px;left:20px}
  .rack-card .cover__rule{top:72px}
  .rack-card .photo--team{top:86px;left:18px;width:204px;height:228px}
  .rack-card .cover__lines{left:100px;top:350px;font-size:13px;line-height:1.35}
  .rack-card .cover__web{bottom:20px;font-size:9px}
</style>
</head>
<body>

<section class="trifold">
  <article class="panel panel--services">
    <div class="photo photo--dominoes" role="img" aria-label="Photo of a hand stopping a falling row of dominoes"></div>
    <div class="services">
      <h2 class="section-title">Turn Key<br>Accounting Services</h2>
      <p>Outsourcing is a business model that can save you time and money by reducing your internal staff, providing you with access to additional intellectual resources, and an external check and balance system.</p>
      <p>The financial benefits of outsourcing include a fixed monthly fee and the elimination of the usual employee benefit costs.</p>
      <p>Our firm offers a wide range of outsourcing services that can be customized to suit your individual needs, from bookkeeping and payroll to full CFO services. Whether you are a small organization or a larger corporation, we can accommodate your needs.</p>
    </div>
    <div class="photo photo--meeting" role="img" aria-label="Photo of business people meeting in front of a presentation screen"></div>
  </article>

  <article class="panel panel--clients">
    <div class="photo photo--analyst" role="img" aria-label="Photo of an accountant working at a laptop"></div>
    <div class="clients">
      <h2 class="section-title">Our Clients</h2>
      <ul class="client-list">
        <li>Not-for-Profit</li><li>Law Firms</li>
        <li>For Profit</li><li>Joint Ventures</li>
        <li>Healthcare</li><li>Individuals</li>
        <li>Physicians</li><li>Small Businesses</li>
        <li>Dentists</li><li>Ledgerfox Users</li>
      </ul>
    </div>
    <div class="contact">
      <div class="brand"><span class="brand__mark"></span><span class="brand__name">Vostran, Pemmel &amp; Co.</span></div>
      <p class="brand__tag">Certified Public Accountants</p>
      <p class="address">482 Harlow Avenue<br>Denton, OH 44120<br>Ph: (440) 555-0148<br>Fax: (440) 555-0149<br>office@vostranpemmel.com</p>
    </div>
  </article>

  <article class="panel cover">
    <div class="brand"><span class="brand__mark"></span><span class="brand__name">Vostran, Pemmel &amp; Co.</span></div>
    <div class="brand-tag-wrap"><p class="brand__tag">Certified Public Accountants</p></div>
    <div class="cover__rule"></div>
    <div class="photo photo--team" role="img" aria-label="Photo of two colleagues reviewing documents at a desk"></div>
    <p class="cover__lines">Providing<br>Accounting,<br>Financial,<br>and Tax Services<br><span class="since">Since 1973</span></p>
    <p class="cover__web">www.vostranpemmel.com</p>
  </article>
</section>

<article class="rack-card cover">
  <div class="brand"><span class="brand__mark"></span><span class="brand__name">Vostran, Pemmel &amp; Co.</span></div>
  <div class="brand-tag-wrap"><p class="brand__tag">Certified Public Accountants</p></div>
  <div class="cover__rule"></div>
  <div class="photo photo--team" role="img" aria-label="Photo of two colleagues reviewing documents at a desk"></div>
  <p class="cover__lines">Providing<br>Accounting,<br>Financial,<br>and Tax Services<br><span class="since">Since 1973</span></p>
  <p class="cover__web">www.vostranpemmel.com</p>
</article>

</body>
</html>
```